Business Card Design

We are a design build firm specializing in the construction and design of kitchens. We are a "green" company, hence the logo. Here are some IDEAS we came up with. I am asking to use this for every person in our firm, so I will need to be able to edit the text. On the back, I am thinking of a very simple design... maybe carry over the white band around the edge. Maybe a simple saying on the back "Renovating homes from Concept to Completion".

Please see our current website for our style and design info
www.cabinetrefitvalley.com (going to be forwarded to maplehearthllc.com)

Industry/Entity Type

Construction

Contact Information for Business Card

Maple Hearth Design & Construction
Dana Wickford - Chief Designer
418 Birchwood Lane
Linden Falls, CT 06990
203.555.0172 C
203.555.0149 O
www.maplehearthllc.com
mhcabinets@mailbox.example

```html
<!DOCTYPE html>
<html lang="en">
<head>
<meta charset="utf-8">
<title>Maple Hearth Design &amp; Construction – Business Card</title>
<link href="https://fonts.googleapis.com/css2?family=Bitter:wght@400;600;700&display=swap" rel="stylesheet">
<style>
  :root {
    --canvas-bg: #ecebe8;
    --lime: #8ff20a;
    --green-mid: #4fa30c;
    --green-deep: #0b2a02;
    --ink: #1c1c1c;
    --white: #ffffff;
    --leaf: #7ed321;
    --card-shadow: rgba(0,0,0,0.18);
  }
  * { margin: 0; padding: 0; box-sizing: border-box; }
  html, body {
    width: 1200px;
    height: 1080px;
    overflow: hidden;
    background: var(--canvas-bg);
    font-family: "Bitter", Georgia, serif;
  }
  .canvas {
    width: 1200px;
    height: 1080px;
    display: flex;
    justify-content: center;
    align-items: center;
    gap: 40px;
  }
  .card {
    width: 500px;
    height: 875px;
    position: relative;
    box-shadow: 0 6px 18px var(--card-shadow);
    text-align: center;
  }

  /* Front */
  .card--front {
    background: linear-gradient(to bottom,
      var(--lime) 0%,
      var(--lime) 50%,
      var(--green-mid) 76%,
      var(--green-deep) 100%);
    color: var(--white);
  }
  .brand {
    display: flex;
    flex-direction: column;
    align-items: center;
    font-weight: 600;
  }
  .brand__dot {
    width: 64px;
    height: 64px;
    border-radius: 50%;
    margin-bottom: 26px;
  }
  .brand__name {
    font-size: 46px;
    letter-spacing: 2px;
    line-height: 1;
  }
  .brand__sub {
    font-size: 21px;
    letter-spacing: 3.5px;
    margin-top: 14px;
    text-transform: uppercase;
  }
  .card--front .brand {
    position: absolute;
    top: 100px;
    left: 0;
    right: 0;
    color: var(--white);
  }
  .card--front .brand__dot { background: var(--white); }

  .person {
    position: absolute;
    top: 405px;
    left: 0;
    right: 0;
  }
  .person__name {
    font-size: 29px;
    font-weight: 700;
  }
  .person__role {
    font-size: 21px;
    margin-top: 10px;
  }
  .person__rule {
    width: 330px;
    height: 2px;
    background: var(--white);
    opacity: 0.8;
    margin: 22px auto 0;
  }

  .contact {
    position: absolute;
    top: 538px;
    left: 0;
    right: 0;
    list-style: none;
    font-size: 22px;
    line-height: 41px;
  }
  .contact__item {
    display: flex;
    justify-content: center;
    align-items: center;
    gap: 10px;
  }
  .contact__icon {
    width: 19px;
    height: 19px;
    flex: none;
  }
  .address {
    position: absolute;
    top: 722px;
    left: 0;
    right: 0;
    font-size: 22px;
    line-height: 32px;
    font-style: normal;
  }

  /* Back */
  .card--back {
    background: var(--white);
    color: var(--ink);
  }
  .card--back .brand {
    position: absolute;
    top: 292px;
    left: 0;
    right: 0;
    color: var(--ink);
  }
  .card--back .brand__dot { background: var(--leaf); }
  .tagline {
    position: absolute;
    top: 560px;
    left: 0;
    right: 0;
    font-size: 33px;
    line-height: 46px;
    font-weight: 400;
  }
</style>
</head>
<body>
<main class="canvas">

  <section class="card card--front" aria-label="Business card front">
    <div class="brand">
      <span class="brand__dot"></span>
      <span class="brand__name">MAPLE HEARTH</span>
      <span class="brand__sub">Design &amp; Construction</span>
    </div>

    <div class="person">
      <h1 class="person__name">Dana Wickford</h1>
      <p class="person__role">Chief Designer</p>
      <div class="person__rule"></div>
    </div>

    <ul class="contact">
      <li class="contact__item">
        <svg class="contact__icon" viewBox="0 0 20 20" fill="none" stroke="#fff" stroke-width="1.8">
          <path d="M5 2 L8 6 L6 8 C7 11 9 13 12 14 L14 12 L18 15 L16 18 C9 18 2 11 2 4 Z"/>
        </svg>
        <span>203.555.0149</span>
      </li>
      <li class="contact__item">
        <svg class="contact__icon" viewBox="0 0 20 20" fill="none" stroke="#fff" stroke-width="1.8">
          <rect x="5" y="1.5" width="10" height="17" rx="1.5"/>
          <line x1="7.5" y1="5" x2="12.5" y2="5"/>
          <circle cx="10" cy="15" r="0.8" fill="#fff"/>
        </svg>
        <span>203.555.0172</span>
      </li>
      <li class="contact__item">
        <svg class="contact__icon" viewBox="0 0 20 20" fill="none" stroke="#fff" stroke-width="1.8">
          <rect x="2" y="5" width="16" height="11" rx="1"/>
          <path d="M2 6 L10 12 L18 6"/>
        </svg>
        <span>mhcabinets@mailbox.example</span>
      </li>
      <li class="contact__item">
        <svg class="contact__icon" viewBox="0 0 20 20" fill="none" stroke="#fff" stroke-width="1.6">
          <circle cx="10" cy="10" r="8"/>
          <ellipse cx="10" cy="10" rx="3.5" ry="8"/>
          <line x1="2" y1="10" x2="18" y2="10"/>
        </svg>
        <span>www.maplehearthllc.com</span>
      </li>
    </ul>

    <address class="address">418 Birchwood Lane Linden Falls<br>CT 06990</address>
  </section>

  <section class="card card--back" aria-label="Business card back">
    <div class="brand">
      <span class="brand__dot"></span>
      <span class="brand__name">MAPLE HEARTH</span>
      <span class="brand__sub">Design &amp; Construction</span>
    </div>
    <p class="tagline">Renovating homes from<br>Concept to Completion</p>
  </section>

</main>
</body>
</html>
```